R. Tanford Realty, Inc business card (2 sided), letterhead (1 sided) & #10 envelope (1 sided)

business card of standard size utilizing the attached logo. Side one with logo, Wade Tanford (my name), President / Broker (title), 805-555-0183 (phone), www.rtanfordrealty.example (website), 1726 Pelham Avenue, Suite 4403 Marlow Bay, CA 93999 (business address) wade.rtanfordrealty@mailbox.example (e-mail address),
Side two - Log

Letterhead and #10 envelope in the same theme

Project Deadline Extended
Reason: I think a 2 day deadline may be a bit ambitious on my part. I have extended the deadline to 4 days. Thanks!

```html
<!DOCTYPE html>
<html lang="en">
<head>
<meta charset="utf-8">
<title>R. Tanford Realty, Inc — Business Card Options</title>
<link href="https://fonts.googleapis.com/css2?family=Crimson+Text:wght@400;600&family=Arimo:wght@400&display=swap" rel="stylesheet">
<style>
  :root {
    --board: #134965;
    --label: #c9d6df;
    --card: #ffffff;
    --brand: #1f73a3;
    --ink: #4a4a4a;
    --icon: #1b6d9c;
    --back-top: #0b8bd0;
    --back-bottom: #075b8e;
    --back-text: #ffffff;
  }
  * { margin: 0; padding: 0; box-sizing: border-box; }
  html, body { width: 1200px; height: 901px; overflow: hidden; }
  body {
    background: var(--board);
    font-family: "Crimson Text", Georgia, serif;
    position: relative;
  }
  .option-label {
    position: absolute;
    left: 15px; width: 100%;
    text-align: center;
    font-family: "Arimo", Arial, sans-serif;
    font-weight: 400;
    font-size: 32px;
    line-height: 1;
    color: var(--label);
  }
  .option-label--top { top: 46px; }
  .option-label--bottom { top: 836px; }

  .card {
    position: absolute;
    width: 538px; height: 313px;
    box-shadow: 0 8px 22px rgba(0,0,0,0.45);
  }
  .card--single { left: 345px; top: 98px; background: var(--card); }
  .card--front { left: 59px; top: 501px; background: var(--card); }
  .card--back {
    left: 619px; top: 501px;
    background: linear-gradient(160deg, var(--back-top) 0%, var(--back-bottom) 75%);
    border: 1px solid #8fc3e4;
  }

  .brand {
    position: absolute;
    display: flex; align-items: center; gap: 9px;
    color: var(--brand);
    font-weight: 400;
    white-space: nowrap;
  }
  .brand__mark { width: 14px; height: 14px; background: var(--brand); flex: none; }
  .card--single .brand { left: 252px; top: 124px; font-size: 25px; }
  .card--front .brand { left: 108px; top: 123px; font-size: 29px; }
  .card--front .brand__mark { width: 16px; height: 16px; }

  .person__name { color: var(--brand); font-weight: 400; }
  .person__title { color: var(--ink); }
  .card--single .person { position: absolute; left: 26px; top: 190px; white-space: nowrap; }
  .card--single .person__name { font-size: 20px; }
  .card--single .person__title { font-size: 12px; margin-left: 6px; }
  .card--front .person {
    position: absolute; left: -22px; width: 100%; top: 226px;
    text-align: center;
  }
  .card--front .person__name { display: block; font-size: 30px; line-height: 1.1; }
  .card--front .person__title { display: block; font-size: 15px; }

  .contact {
    position: absolute; list-style: none;
    --icon-bg: var(--icon);
    --icon-fg: #ffffff;
  }
  .contact li {
    display: flex; align-items: flex-start; gap: 8px;
    font-size: 14.5px; line-height: 1.25; white-space: nowrap;
  }
  .contact svg { width: 15px; height: 15px; flex: none; margin-top: 2px; }
  .card--single .contact { color: var(--ink); }
  .card--single .contact li { min-height: 23px; }
  .card--single .contact--main { left: 24px; top: 226px; }
  .card--single .contact--address { left: 303px; top: 255px; }
  .card--back .contact {
    left: 33px; top: 182px; color: var(--back-text);
    --icon-bg: #ffffff;
    --icon-fg: var(--back-bottom);
  }
  .card--back .contact li { font-size: 15px; margin-bottom: 3px; }

  .icon-bg { fill: var(--icon-bg); }
  .icon-glyph { fill: var(--icon-fg); }
  .icon-line { stroke: var(--icon-bg); stroke-width: 0.8; fill: none; }
</style>
</head>
<body>
  <svg width="0" height="0" style="position:absolute">
    <defs>
      <symbol id="i-phone" viewBox="0 0 16 16"><circle class="icon-bg" cx="8" cy="8" r="8"/><path class="icon-glyph" d="M5.2 3.6l1.4 0 0.8 2.1-1 0.9c0.5 1.1 1.2 1.9 2.2 2.4l0.9-1 2.1 0.8 0 1.4c0 0.5-0.5 1-1 1-3.6-0.2-6.3-3-6.5-6.6 0-0.5 0.5-1 1.1-1z"/></symbol>
      <symbol id="i-mail" viewBox="0 0 16 16"><circle class="icon-bg" cx="8" cy="8" r="8"/><rect class="icon-glyph" x="4" y="5" width="8" height="6"/><path class="icon-line" d="M4.4 5.4L8 8.4l3.6-3"/></symbol>
      <symbol id="i-web" viewBox="0 0 16 16"><circle class="icon-bg" cx="8" cy="8" r="8"/><circle class="icon-glyph" cx="8" cy="8" r="4.2"/><path class="icon-line" d="M3.8 8h8.4M8 3.8c-1.6 2.4-1.6 6 0 8.4M8 3.8c1.6 2.4 1.6 6 0 8.4"/></symbol>
      <symbol id="i-home" viewBox="0 0 16 16"><circle class="icon-bg" cx="8" cy="8" r="8"/><path class="icon-glyph" d="M8 3.6l4.2 3.8h-1.2v4.4H9.2V9H6.8v2.8H5V7.4H3.8z"/></symbol>
    </defs>
  </svg>

  <h2 class="option-label option-label--top">Front single side_opt 1</h2>

  <section class="card card--single" aria-label="Single-sided card">
    <div class="brand"><span class="brand__mark"></span>R. Tanford Realty, Inc</div>
    <p class="person"><span class="person__name">Wade Tanford</span><span class="person__title">President | Broker</span></p>
    <ul class="contact contact--main">
      <li><svg><use href="#i-phone"/></svg>805-555-0183</li>
      <li><svg><use href="#i-mail"/></svg>wade.rtanfordrealty@mailbox.example</li>
      <li><svg><use href="#i-web"/></svg>www.rtanfordrealty.example</li>
    </ul>
    <ul class="contact contact--address">
      <li><svg><use href="#i-home"/></svg><span>#1726 Pelham Avenue, Suite 4403<br>Marlow Bay, CA 93999</span></li>
    </ul>
  </section>

  <section class="card card--front" aria-label="Card front">
    <div class="brand"><span class="brand__mark"></span>R. Tanford Realty, Inc</div>
    <p class="person"><span class="person__name">Wade Tanford</span><span class="person__title">President | Broker</span></p>
  </section>

  <section class="card card--back" aria-label="Card back">
    <ul class="contact">
      <li><svg><use href="#i-phone"/></svg>805-555-0183</li>
      <li><svg><use href="#i-mail"/></svg>wade.rtanfordrealty@mailbox.example</li>
      <li><svg><use href="#i-web"/></svg>www.rtanfordrealty.example</li>
      <li><svg><use href="#i-home"/></svg><span>#1726 Pelham Avenue, Suite 4403<br>Marlow Bay, CA 93999</span></li>
    </ul>
  </section>

  <h2 class="option-label option-label--bottom">Front&amp;Back_opt 2</h2>
</body>
</html>
```